MossVane Spa, Skincare and Cosmetics website

I need a website for MossVane (putting the glow back into people's skin) which allows viewers to access information about Beauty Spa packaging and facilities as well as online skincare and cosmetic products. Our distinctive difference is that our products are certified organic. We want to target a luxury high income niche market (age 30-50). I want all colours to be "baby colours" preferably background to be "baby metallic pink" (but please don't make the website too immature) with curves as patterns. I want a romantic vintage look.

The website needs to look:
1. elegant (prestige and luxury)
2. bright (baby colours mainly)
3. European curves and signature patterns
4. Can include Pearl related pics (but not a must)

The website pages needs to have:
1. pages ordering skincare/cosmetics
2. shopping cart and payment
3. about us and about our product differences
4. contact us
5. booking for spa treatments and packages

I have attached our logo and also packaging label styles.

Industry/Entity Type

Cosmetics

```html
<!DOCTYPE html>
<html lang="en">
<head>
<meta charset="utf-8">
<title>MossVane Spa, Skincare and Cosmetics</title>
<link href="https://fonts.googleapis.com/css2?family=Cinzel:wght@400;600&family=Great+Vibes&family=Pinyon+Script&family=Open+Sans:wght@400;600&display=swap" rel="stylesheet">
<style>
:root{
  --page:#ffffff;
  --blush:#e9a9b8;
  --blush-deep:#d98a9e;
  --blush-soft:#f6e6ea;
  --lace:#f3ebe8;
  --ink:#3a3a3a;
  --ink-soft:#8a8a8a;
  --rule:#d9d4d4;
  --charcoal:#4a4a4a;
  --skin:#e8c9b8;
  --towel:#f4f2f0;
  --leaf:#8ec63f;
}
*{box-sizing:border-box;margin:0;padding:0}
html,body{width:1200px;height:2250px;overflow:hidden;background:var(--page)}
body{position:relative;font-family:"Open Sans",Arial,sans-serif;color:var(--ink)}
.abs{position:absolute}

/* header */
.lace-top{left:0;top:0;width:1200px;height:150px;background:linear-gradient(180deg,var(--lace),#fbf7f6)}
.brand{left:188px;top:40px;display:flex;align-items:center;gap:14px}
.brand-dot{width:34px;height:34px;border-radius:50%;background:var(--blush)}
.brand-name{font-family:"Cinzel",serif;font-size:40px;color:var(--blush-deep);font-weight:400;letter-spacing:1px}
.social{left:890px;top:8px;display:flex;gap:12px}
.social span{width:30px;height:30px;border-radius:5px;background:var(--blush)}
.nav{left:608px;top:95px;display:flex;gap:4px;font-family:"Cinzel",serif;font-size:15px}
.nav a{color:var(--blush-deep);text-decoration:none;padding:6px 10px}
.nav a.active{background:var(--blush);color:#fff}

/* hero */
.hero{left:0;top:150px;width:1200px;height:520px;background:
  radial-gradient(ellipse at 38% 35%,var(--skin) 0 22%,transparent 40%),
  linear-gradient(90deg,#b9977e 0%,#e2c7b4 30%,var(--towel) 65%,#ffffff 100%)}
.hero-band{left:0;top:522px;width:1200px;height:66px;background:rgba(233,169,184,.55);display:flex;align-items:center;justify-content:center}
.hero-band p{font-family:"Great Vibes",cursive;font-size:44px;color:#fff;letter-spacing:1px}
.lace-bottom{left:0;top:650px;width:1200px;height:125px;background:linear-gradient(180deg,var(--lace),#fdfafa)}

/* section heads */
.section-title{left:0;width:1200px;text-align:center;font-family:"Pinyon Script",cursive;font-size:54px;line-height:1}
.section-title .lead{color:var(--charcoal)}
.section-title .accent{color:var(--blush-deep)}
.rule{left:168px;width:865px;height:1px;background:var(--rule)}

/* specials */
.special{top:863px;height:200px;border:4px solid #eee}
.special-photo{background:radial-gradient(ellipse at 50% 45%,#faf7f2 0 28%,#e9cdbb 45%,#d6ab92 100%)}
.special-feature{background:linear-gradient(180deg,#6a6a6a,#9a9a9a)}
.special-feature .cap{position:absolute;left:0;top:0;width:100%;height:100%;background:rgba(60,60,60,.75);padding:12px 14px;color:#eee}
.special-feature h3{font-family:"Pinyon Script",cursive;font-weight:400;font-size:36px;color:#fff;line-height:1.1;margin-bottom:6px}
.special-feature p{font-size:11px;line-height:1.45}
.special-feature .more{position:absolute;right:12px;bottom:8px;font-size:11px}

/* products */
.product{top:1263px;width:210px}
.product-shot{width:150px;height:190px;margin-left:30px;background:linear-gradient(180deg,#c7e58a 0 25%,#f3eee9 25% 75%,#d9cbd2 100%);border-radius:18px 18px 6px 6px;position:relative}
.product-shot .tag{position:absolute;left:35px;top:96px;background:var(--blush);color:#fff;font-size:11px;padding:4px 10px}
.product h4{margin-top:30px;font-size:15px;font-weight:600;color:var(--ink)}
.product p{margin-top:12px;font-size:11px;line-height:1.35;color:var(--ink-soft)}

/* about + features */
.block-title{font-family:"Pinyon Script",cursive;font-size:44px;color:var(--charcoal);line-height:1}
.about{left:168px;top:1688px;width:285px}
.about p{margin-top:20px;font-size:12px;line-height:1.85;color:var(--ink-soft)}
.features{left:488px;top:1688px;width:260px}
.features ul{list-style:none;margin-top:20px}
.features li{font-size:13px;color:var(--ink-soft);line-height:2.05;display:flex;align-items:center;gap:14px}
.features li::before{content:"";width:14px;height:2px;background:var(--blush-deep)}
.certified{left:755px;top:1700px;width:278px;height:188px;background:linear-gradient(90deg,#dfe8d4 0%,#f7f5f2 45%,#eef3e8 100%)}
.certified .seal{position:absolute;right:22px;top:26px;width:108px;height:108px;border-radius:50%;background:var(--leaf);opacity:.85}

/* footer */
.foot-title{font-family:"Cinzel",serif;font-size:13px;color:var(--ink);border-bottom:1px solid var(--rule);padding-bottom:8px}
.sitemap{left:168px;top:2025px;width:115px}
.sitemap ul{list-style:none;margin-top:8px}
.sitemap li{font-family:"Cinzel",serif;font-size:10px;color:var(--ink-soft);border-bottom:1px solid #eee;line-height:1.75}
.info{left:313px;top:2025px;width:440px}
.info ul{list-style:none;margin-top:14px}
.info li{font-family:"Cinzel",serif;font-size:10px;color:var(--ink-soft);line-height:1.6;display:flex;gap:8px}
.info li svg{flex:none;margin-top:3px}
.map{left:538px;top:2070px;width:200px;height:85px;background:#e6e1e1;font-size:10px;color:var(--ink-soft);padding:8px 10px}
.newsletter{left:758px;top:2025px;width:275px}
.newsletter p{margin-top:14px;font-family:"Cinzel",serif;font-size:10px;color:var(--ink-soft)}
.field{margin:8px 0 0 20px;width:250px;height:22px;background:var(--blush-soft);font-family:"Cinzel",serif;font-size:9px;color:var(--ink-soft);padding:5px 10px}
.submit{margin:8px 0 0 110px;width:75px;height:22px;background:var(--blush);color:#fff;font-family:"Cinzel",serif;font-size:9px;display:flex;align-items:center;justify-content:center}
.copyright{left:168px;top:2222px;font-family:"Cinzel",serif;font-size:9px;color:var(--ink-soft)}
</style>
</head>
<body>

<header>
  <div class="abs lace-top" role="img" aria-label="Soft vintage lace pattern in pale blush"></div>
  <div class="abs brand"><span class="brand-dot"></span><span class="brand-name">MossVane</span></div>
  <div class="abs social" aria-label="Social links"><span></span><span></span><span></span></div>
  <nav class="abs nav">
    <a class="active" href="#">Home</a><a href="#">Skincare</a><a href="#">Cosmetics</a><a href="#">Products</a><a href="#">About</a><a href="#">Contact</a>
  </nav>
</header>

<section>
  <div class="abs hero" role="img" aria-label="Photo of a relaxing facial massage on a spa bed with white towels and pink flowers"></div>
  <div class="abs lace-bottom" role="img" aria-label="Torn paper edge over vintage lace pattern"></div>
  <div class="abs hero-band"><p>We Put the Glow Back into People's Skin</p></div>
</section>

<section>
  <h2 class="abs section-title" style="top:735px"><span class="lead">Our</span> <span class="accent">Specials</span></h2>
  <div class="abs rule" style="top:825px"></div>

  <article class="abs special special-feature" style="left:168px;width:275px">
    <div class="cap">
      <h3>Lorem Ipsum</h3>
      <p>Lorem ipsum dolor sit amet, consectetur adip-iscing elit, sed do eiusmod tempor incididunt ut labore et dolore magna aliqua. Ut enim ad minim veniam, quis</p>
      <span class="more">View</span>
    </div>
  </article>
  <div class="abs special special-photo" style="left:458px;width:280px" role="img" aria-label="Photo of a woman receiving a white facial mask treatment"></div>
  <div class="abs special special-photo" style="left:755px;width:278px" role="img" aria-label="Photo of a woman receiving a white facial mask treatment"></div>
</section>

<section>
  <h2 class="abs section-title" style="top:1110px"><span class="lead">Organic</span> <span class="accent">Products</span></h2>
  <div class="abs rule" style="top:1195px"></div>

  <article class="abs product" style="left:168px">
    <div class="product-shot" role="img" aria-label="Product photo of organic skincare bottles"><span class="tag">MORE</span></div>
    <h4>Product Name 1</h4>
    <p>Lorem ipsum dolor sit amet, csecter adipiscing elit, sed do eiusmod tempor incididunt ut l</p>
  </article>
  <article class="abs product" style="left:393px">
    <div class="product-shot" role="img" aria-label="Product photo of organic skincare bottles"></div>
    <h4>Product Name 2</h4>
    <p>Lorem ipsum dolor sit amet, csecter adipiscing elit, sed do eiusmod tempor incididunt ut l</p>
  </article>
  <article class="abs product" style="left:618px">
    <div class="product-shot" role="img" aria-label="Product photo of organic skincare bottles"></div>
    <h4>Product Name 3</h4>
    <p>Lorem ipsum dolor sit amet, csecter adipiscing elit, sed do eiusmod tempor incididunt ut l</p>
  </article>
  <article class="abs product" style="left:843px">
    <div class="product-shot" role="img" aria-label="Product photo of organic skincare bottles"></div>
    <h4>Product Name 4</h4>
    <p>Lorem ipsum dolor sit amet, csecter adipiscing elit, sed do eiusmod tempor incididunt ut l</p>
  </article>

  <div class="abs rule" style="top:1625px"></div>
</section>

<section>
  <div class="abs about">
    <h2 class="block-title">About us:</h2>
    <p>Lorem ipsum dolor sit amet, consectetur adipiscing elit, sed do eiusmod tempor incidid unt ut labore et dolore magna aliqua. Ut enim ad minim veniam, quis nostrud exercitation ullamco laboris nisi ut aliquip ex ea commodo consequat. Duis aute irure dolor in reprehen-derit in voluptate velit esse cillum dolore eu fugiat nulla pariatur.</p>
  </div>
  <div class="abs features">
    <h2 class="block-title">Features:</h2>
    <ul>
      <li>Lorem ipsum dolor sit</li>
      <li>Sed ut perspiciatis unde</li>
      <li>Lorem ipsum dolor sit</li>
      <li>Sed ut perspiciatis unde</li>
      <li>Lorem ipsum dolor sit</li>
      <li>Sed ut perspiciatis unde</li>
    </ul>
  </div>
  <div class="abs certified" role="img" aria-label="Photo of organic products with green leaves and a certification seal"><span class="seal"></span></div>
  <div class="abs rule" style="top:1988px"></div>
</section>

<footer>
  <div class="abs sitemap">
    <h3 class="foot-title">Sitemap</h3>
    <ul><li>Home</li><li>Skincare</li><li>Cosmetics</li><li>Products</li><li>Contact</li></ul>
  </div>
  <div class="abs info">
    <h3 class="foot-title" style="width:200px">Our Info</h3>
    <ul>
      <li><svg width="9" height="11" viewBox="0 0 9 11"><path d="M4.5 0A4 4 0 0 0 .5 4c0 3 4 7 4 7s4-4 4-7a4 4 0 0 0-4-4z" fill="#8a8a8a"/><circle cx="4.5" cy="4" r="1.5" fill="#fff"/></svg><span>Address Line 11<br>Country, State</span></li>
      <li style="margin-top:10px"><svg width="9" height="9" viewBox="0 0 9 9"><rect x="1" y="0" width="7" height="9" rx="1.5" fill="#8a8a8a"/></svg><span>000.000.000</span></li>
      <li><svg width="9" height="9" viewBox="0 0 9 9"><rect x="0" y="1.5" width="9" height="6" fill="#8a8a8a"/><path d="M0 1.5l4.5 3.5 4.5-3.5" stroke="#fff" fill="none"/></svg><span>hello@mossvane.example</span></li>
    </ul>
  </div>
  <div class="abs map" role="img" aria-label="Map showing the spa location">Map</div>
  <div class="abs newsletter">
    <h3 class="foot-title">Our Info</h3>
    <p>Get our latest news and be up to date.</p>
    <div class="field">Name</div>
    <div class="field">Email</div>
    <div class="submit">Submit</div>
  </div>
  <div class="abs rule" style="top:2210px"></div>
  <p class="abs copyright">Copyright © 2014 MossVane. All rights reserved.</p>
</footer>

</body>
</html>
```